Your conflict - our mediation - joint conflict SOLUTION

With this flyer I am looking for conflict parties who are ready to tackle and resolve their conflict with a prospective mediator. The mediation is free because I am doing it as part of my diploma thesis. Time frame approx. 4 sessions of 2.5 hours each. The wishes and needs of both parties are listened to and “picked out”. In an open, constructive, appreciative framework, solutions are developed and negotiated together.

Target Market(s)

everyone who is ready to deal with himself and his counterpart and everyone who wants to work out a solution with the respect, openness and support of a mediator.

Requirements
Must have
• - "For my diploma thesis I am looking for conflicting parties who are willing to resolve their conflict with a mediator"
- Time frame: 4 x 2.5 hours feasible in Solothurn, Bern, Brugg
- Free of charge
- my coordinates - see business card
- more information at www.talweidenhof.ch
Nice to have
• the card should be based on the style of my homepage www.talweidenhof.ch and my business card

```html
<!DOCTYPE html>
<html lang="en">
<head>
<meta charset="utf-8">
<title>Mediation Flyer – Talweidenhof</title>
<link rel="stylesheet" href="https://fonts.googleapis.com/css2?family=Montserrat:wght@400;500;700;800&display=swap">
<style>
  :root {
    --stage: #6a6a6a;
    --paper: #ffffff;
    --plum-dark: #432c55;
    --plum-mid: #735a88;
    --plum-head: #7a5c96;
    --gold: #a88a55;
    --photo-light: #f3ece6;
    --photo-warm: #d9b9a1;
    --ink-light: #ffffff;
  }
  * { margin: 0; padding: 0; box-sizing: border-box; }
  html, body { width: 1029px; height: 1200px; overflow: hidden; }
  body { background: var(--stage); font-family: "Montserrat", sans-serif; }

  .flyer {
    position: absolute; left: 51px; top: 0;
    width: 927px; height: 1200px;
    background: var(--paper); overflow: hidden;
  }
  .hero-photo {
    position: absolute; left: 0; top: 0; width: 560px; height: 593px;
    background: radial-gradient(ellipse at 45% 55%, var(--photo-warm) 0%, #ead7c8 45%, var(--photo-light) 75%, #ffffff 100%);
  }
  .brand {
    position: absolute; left: 566px; top: 110px;
    display: flex; align-items: center; gap: 14px;
    font-weight: 500; font-size: 38px; color: var(--gold);
  }
  .brand-dot { width: 22px; height: 22px; border-radius: 50%; background: var(--gold); }

  .headline-top {
    position: absolute; left: 560px; top: 270px; width: 325px;
    font-weight: 800; font-size: 66px; line-height: 1; color: var(--plum-head);
    text-align: center; letter-spacing: -1px;
  }
  .headline-box {
    position: absolute; left: 562px; top: 340px; width: 318px; height: 81px;
    background: var(--plum-dark); border-radius: 3px;
    color: var(--ink-light); font-weight: 800; font-size: 62px;
    display: flex; align-items: center; justify-content: center; letter-spacing: -1px;
  }
  .hero-rule { position: absolute; left: 567px; top: 455px; width: 319px; height: 1px; background: var(--plum-dark); }
  .subline {
    position: absolute; left: 566px; top: 464px;
    font-weight: 700; font-size: 31px; color: var(--plum-dark); white-space: nowrap;
  }
  .subline-strong {
    position: absolute; left: 563px; top: 502px;
    font-weight: 800; font-size: 61px; color: var(--plum-dark); letter-spacing: -1px;
  }

  .offer-band {
    position: absolute; left: 0; top: 593px; width: 927px; height: 111px;
    background: var(--plum-dark); color: var(--ink-light);
    display: flex; align-items: center; justify-content: center;
    font-weight: 800; font-size: 62px; letter-spacing: 9px;
  }
  .details {
    position: absolute; left: 0; top: 704px; width: 927px; height: 397px;
    background: var(--plum-mid); color: var(--ink-light);
  }
  .intro {
    position: absolute; left: 40px; top: 24px; width: 847px;
    text-align: center; font-weight: 500; font-size: 25px; line-height: 32.5px;
  }
  .timeframe-label {
    position: absolute; left: 96px; top: 167px; width: 300px; height: 49px;
    background: var(--paper); color: var(--plum-dark);
    font-weight: 800; font-size: 32px; display: flex; align-items: center; justify-content: center;
  }
  .timeframe-hours { position: absolute; left: 96px; top: 234px; font-weight: 700; font-size: 37px; }
  .timeframe-places { position: absolute; left: 96px; top: 283px; font-weight: 500; font-size: 28px; line-height: 35px; }
  .divider { position: absolute; left: 476px; top: 164px; width: 1.5px; height: 192px; background: var(--ink-light); }
  .quote-frame { position: absolute; left: 530px; top: 130px; width: 320px; height: 260px; }
  .quote-text {
    position: absolute; left: 565px; top: 199px; width: 270px;
    font-weight: 500; font-size: 18px; line-height: 22px;
  }

  .footer {
    position: absolute; left: 0; top: 1101px; width: 927px; height: 99px;
    background: var(--plum-dark); color: var(--ink-light);
    font-weight: 500; font-size: 23px;
  }
  .footer-label { position: absolute; left: 111px; top: 34px; }
  .footer-sep { position: absolute; left: 440px; top: 37px; width: 1.5px; height: 27px; background: var(--ink-light); }
  .footer-url { position: absolute; left: 478px; top: 34px; }
</style>
</head>
<body>
  <main class="flyer">
    <div class="hero-photo" role="img" aria-label="Photo of a happy family: a laughing father carrying his little daughter on his shoulders while the mother smiles at them"></div>

    <div class="brand"><span class="brand-dot"></span>Talweidenhof</div>

    <div class="headline-top">ARE YOU</div>
    <div class="headline-box">STUCK?</div>
    <div class="hero-rule"></div>
    <div class="subline">need conflict with a</div>
    <div class="subline-strong">MEDIATOR</div>

    <div class="offer-band">FREE OF CHARGE</div>

    <section class="details">
      <p class="intro">For my diploma thesis I am looking for<br>conflicting parties who are willing to resolve their conflict<br>with a mediator</p>

      <div class="timeframe-label">TIME FRAME:</div>
      <div class="timeframe-hours">4 x 2.5 hours</div>
      <div class="timeframe-places">feasible in Solothurn,<br>Bern, Brugg</div>

      <div class="divider"></div>

      <svg class="quote-frame" viewBox="0 0 320 260" aria-hidden="true">
        <path d="M28 50 H8 V215 H250 M296 215 H308 V50 H100" fill="none" stroke="#ffffff" stroke-width="1.5"/>
        <text x="30" y="110" font-family="Georgia, serif" font-size="110" fill="none" stroke="#ffffff" stroke-width="1.5">&#8220;</text>
        <text x="244" y="300" font-family="Georgia, serif" font-size="110" fill="none" stroke="#ffffff" stroke-width="1.5">&#8221;</text>
      </svg>
      <p class="quote-text">Because your own conflict makes you less able to think, feel and act, it is worthwhile to be accompanied by a mediator.</p>
    </section>

    <footer class="footer">
      <span class="footer-label">For More Information at</span>
      <span class="footer-sep"></span>
      <span class="footer-url">www.talweidenhof.ch</span>
    </footer>
  </main>
</body>
</html>
```